Design an Outstanding flyer for my company.

I need a flyer designed for our window tinting company based in Brisbane Queensland Australia. The flyer will be targeting Home tinting. We also do mobile car tinting. Something in regards to this could be incorporated into the flyer as well.
I want it to be 2 sided DL size. Black background.
It really needs to Pop, and be a real attention getter.
It needs to be easy to read.
I have provided a mock up with the info on it from our marketing company. It will need a spellcheck etc to make sure everything is correct.
Everything about it can be changed however you like.
I have also included the company logo.

Lets see what you've got!

Target Market(s)

Home Owners

Industry/Entity Type

Home Improvement

Other font styles liked:
• Duan Penh

Requirements
Must have
• All the information on the mock up. Clear and easy to read.
• Must Stand Out!

```html
<!DOCTYPE html>
<html lang="en">
<head>
<meta charset="utf-8">
<title>Brightline Window Tinting – DL Flyer</title>
<link rel="stylesheet" href="https://fonts.googleapis.com/css2?family=Teko:wght@600;700&family=Russo+One&family=Exo+2:wght@500;700&family=Roboto+Condensed:wght@300;400&display=swap">
<style>
  :root{
    --page:#e4e4e4;
    --panel:#131313;
    --panel-band:#1b1b1b;
    --panel-foot:#070707;
    --yellow:#f4ec1a;
    --gold:#e4c64a;
    --gold-deep:#b08b1c;
    --white:#ffffff;
    --body-text:#d6d6d6;
    --silver-light:#ffffff;
    --silver-mid:#bfc3c7;
    --silver-dark:#6d7176;
    --divider:#2c2c2c;
  }
  *{box-sizing:border-box;margin:0;padding:0}
  html,body{width:1134px;height:1200px;overflow:hidden;background:var(--page)}
  .sheet{position:relative;width:1134px;height:1200px}

  .flyer{
    position:absolute;top:72px;width:498px;height:1055px;
    background:var(--panel);overflow:hidden;
    box-shadow:0 6px 18px rgba(0,0,0,.35);
  }
  .flyer--front{left:47px}
  .flyer--back{left:589px}
  .flyer > *{position:absolute}

  /* textured bands */
  .band{left:0;width:100%;background:linear-gradient(180deg,var(--panel-band),#111 60%,var(--panel-band))}
  .band::before,.band::after{
    content:"";position:absolute;left:50%;transform:translateX(-50%);
    width:120px;height:8px;background:linear-gradient(180deg,#4a4a4a,#2a2a2a);
    clip-path:polygon(0 0,100% 0,50% 100%);
  }
  .band::before{top:14px}
  .band::after{bottom:-8px;opacity:.8}
  .footer-band{left:0;width:100%;bottom:0;height:228px;background:var(--panel-foot);border-top:1px solid var(--divider)}

  /* headline stack */
  .headline{left:0;width:100%;text-align:center;line-height:1}
  .headline__heat{
    display:block;font-family:"Teko",sans-serif;font-weight:700;font-size:82px;letter-spacing:2px;
    background:linear-gradient(180deg,#fff6cf 0%,#e7c760 38%,#8a6a14 52%,#f3dd8a 70%,#b38c24 100%);
    -webkit-background-clip:text;background-clip:text;color:transparent;height:64px;
  }
  .headline__uv{
    display:block;font-family:"Russo One",sans-serif;font-size:35px;letter-spacing:1px;color:var(--yellow);margin-top:4px;
  }
  .headline__money{
    display:block;font-family:"Teko",sans-serif;font-weight:600;font-size:96px;letter-spacing:3px;height:78px;margin-top:4px;
    background:linear-gradient(180deg,#ffffff 0%,#d9dcdf 40%,#5d6166 55%,#eef0f2 72%,#9a9ea3 100%);
    -webkit-background-clip:text;background-clip:text;color:transparent;
  }
  .headline__privacy{
    display:block;font-family:"Exo 2",sans-serif;font-weight:700;font-size:33px;letter-spacing:7px;color:var(--white);margin-top:8px;
  }

  .benefits{
    left:30px;width:438px;font-family:"Roboto Condensed",sans-serif;font-weight:300;
    font-size:18.5px;line-height:24.7px;color:var(--body-text);text-align:justify;text-align-last:center;
  }

  /* 20 reasons ribbon */
  .reasons{left:47px;width:400px;height:74px}
  .reasons__ribbon{position:absolute;left:0;top:0}
  .reasons__count{
    position:absolute;left:0;top:-6px;font-family:"Teko",sans-serif;font-weight:700;font-size:100px;line-height:1;
    background:linear-gradient(180deg,#ffffff 0%,#cfd2d6 45%,#4f5358 58%,#e6e8ea 80%,#8d9196 100%);
    -webkit-background-clip:text;background-clip:text;color:transparent;
  }
  .reasons__text{
    position:absolute;left:85px;top:12px;font-family:"Exo 2",sans-serif;font-weight:500;font-size:20px;line-height:25px;color:#111;
  }

  .call{left:0;width:100%;height:60px}
  .call__text{
    position:absolute;left:0;width:100%;text-align:center;font-family:"Russo One",sans-serif;font-size:21px;
    line-height:28px;letter-spacing:1px;color:var(--gold);
  }
  .call__chevrons{position:absolute;top:12px}
  .call__chevrons--left{left:2px}
  .call__chevrons--right{right:2px}

  .contact{left:0;width:100%;font-family:"Exo 2",sans-serif;font-weight:700;color:var(--white);line-height:1}
  .contact__line{display:flex;align-items:center;justify-content:center;gap:12px;font-size:47px;height:53px}
  .contact__icon{flex:none}

  .brand{left:0;width:100%;top:870px;display:flex;align-items:center;justify-content:center;gap:16px}
  .brand__dot{width:58px;height:58px;border-radius:50%;background:var(--gold);flex:none}
  .brand__name{font-family:"Exo 2",sans-serif;font-weight:700;font-size:31px;letter-spacing:1px;color:var(--gold);line-height:1}

  .web{
    left:68px;width:362px;height:42px;top:990px;border:2px solid var(--gold-deep);border-radius:21px;
    display:flex;align-items:center;justify-content:center;
    font-family:"Roboto Condensed",sans-serif;font-weight:400;font-size:22px;letter-spacing:1px;color:var(--white);
  }

  /* front positions */
  .flyer--front .headline{top:24px}
  .flyer--front .band{top:262px;height:232px}
  .flyer--front .benefits{top:306px}
  .flyer--front .reasons{top:537px}
  .flyer--front .call{top:632px}
  .flyer--front .contact{top:712px}

  /* back positions */
  .flyer--back .reasons{top:28px}
  .flyer--back .headline{top:124px}
  .flyer--back .band{top:362px;height:240px}
  .flyer--back .benefits{top:413px}
  .flyer--back .call{top:645px}
  .flyer--back .contact{top:712px}
</style>
</head>
<body>
<main class="sheet">

  <!-- FRONT SIDE -->
  <section class="flyer flyer--front" aria-label="Flyer front">
    <div class="band"></div>
    <div class="footer-band"></div>

    <h1 class="headline">
      <span class="headline__heat">KEEP HEAT OUT</span>
      <span class="headline__uv">BLOCK 99.9% UV RAYS</span>
      <span class="headline__money">$AVE MONEY</span>
      <span class="headline__privacy">INCREASE PRIVACY</span>
    </h1>

    <p class="benefits">Reduce glare. Reduce energy costs. Control the amount of light entering your home. Reduce carbon footprint. Make home more beautiful. Eliminate home hot spots. Protect against broken glass. Regulate energy. Protects upholstery. Improve effectiveness of roof insulation. Improve health. Reduces interior floor fading. Eliminate need for blinds. Strengthen your windows. Insulate in winter. Affordable.</p>

    <div class="reasons">
      <svg class="reasons__ribbon" width="400" height="74" viewBox="0 0 400 74" aria-hidden="true">
        <defs>
          <linearGradient id="ribbonFront" x1="0" y1="0" x2="0" y2="1">
            <stop offset="0" stop-color="#ffffff"/><stop offset=".55" stop-color="#d4d7da"/><stop offset="1" stop-color="#8e9297"/>
          </linearGradient>
        </defs>
        <polygon points="70,12 372,12 394,70 70,70" fill="url(#ribbonFront)"/>
      </svg>
      <span class="reasons__count">20</span>
      <span class="reasons__text">Reasons why home window<br>tinting is perfect for you.</span>
    </div>

    <div class="call">
      <svg class="call__chevrons call__chevrons--left" width="66" height="34" viewBox="0 0 66 34" aria-hidden="true">
        <g fill="none" stroke="#4a4a4a" stroke-width="5"><path d="M18 3 4 17l14 14"/><path d="M34 3 20 17l14 14"/><path d="M50 3 36 17l14 14"/><path d="M66 3 52 17l14 14"/></g>
      </svg>
      <p class="call__text">CALL BRISBANE’S LEADER IN<br>HOME WINDOW TINTING NOW</p>
      <svg class="call__chevrons call__chevrons--right" width="66" height="34" viewBox="0 0 66 34" aria-hidden="true">
        <g fill="none" stroke="#4a4a4a" stroke-width="5"><path d="M0 3l14 14L0 31"/><path d="M16 3l14 14-14 14"/><path d="M32 3l14 14-14 14"/><path d="M48 3l14 14-14 14"/></g>
      </svg>
    </div>

    <div class="contact">
      <p class="contact__line">
        <svg class="contact__icon" width="24" height="28" viewBox="0 0 24 28" aria-hidden="true"><path d="M7 2 3 5c-2 6 4 17 12 21l4-3-4-6-3 2c-3-2-5-6-6-10l3-2z" fill="none" stroke="#c9a949" stroke-width="2"/></svg>
        07 3000 1234
      </p>
      <p class="contact__line">
        <svg class="contact__icon" width="30" height="22" viewBox="0 0 30 22" aria-hidden="true"><g fill="none" stroke="#c9a949" stroke-width="2"><rect x="1" y="1" width="28" height="20"/><path d="M1 1l14 11L29 1M1 21l10-10M29 21 19 11"/></g></svg>
        0400 555 018
      </p>
    </div>

    <div class="brand">
      <span class="brand__dot"></span>
      <span class="brand__name">BRIGHTLINE WINDOW TINTING</span>
    </div>
    <p class="web">www.brightlinetinting.com.au</p>
  </section>

  <!-- BACK SIDE -->
  <section class="flyer flyer--back" aria-label="Flyer back">
    <div class="band"></div>
    <div class="footer-band"></div>

    <div class="reasons">
      <svg class="reasons__ribbon" width="400" height="74" viewBox="0 0 400 74" aria-hidden="true">
        <defs>
          <linearGradient id="ribbonBack" x1="0" y1="0" x2="0" y2="1">
            <stop offset="0" stop-color="#ffffff"/><stop offset=".55" stop-color="#d4d7da"/><stop offset="1" stop-color="#8e9297"/>
          </linearGradient>
        </defs>
        <polygon points="70,12 372,12 394,70 70,70" fill="url(#ribbonBack)"/>
      </svg>
      <span class="reasons__count">20</span>
      <span class="reasons__text">Reasons why home window<br>tinting is perfect for you.</span>
    </div>

    <h2 class="headline">
      <span class="headline__heat">KEEP HEAT OUT</span>
      <span class="headline__uv">BLOCK 99.9% UV RAYS</span>
      <span class="headline__money">$AVE MONEY</span>
      <span class="headline__privacy">INCREASE PRIVACY</span>
    </h2>

    <p class="benefits">Reduce glare. Reduce energy costs. Control the amount of light entering your home. Reduce carbon footprint. Make home more beautiful. Eliminate home hot spots. Protect against broken glass. Regulate energy. Protects upholstery. Improve effectiveness of roof insulation. Improve health. Reduces interior floor fading. Eliminate need for blinds. Strengthen your windows. Insulate in winter. Affordable.</p>

    <div class="call">
      <svg class="call__chevrons call__chevrons--left" width="66" height="34" viewBox="0 0 66 34" aria-hidden="true">
        <g fill="none" stroke="#4a4a4a" stroke-width="5"><path d="M18 3 4 17l14 14"/><path d="M34 3 20 17l14 14"/><path d="M50 3 36 17l14 14"/><path d="M66 3 52 17l14 14"/></g>
      </svg>
      <p class="call__text">CALL BRISBANE’S LEADER IN<br>HOME WINDOW TINTING NOW</p>
      <svg class="call__chevrons call__chevrons--right" width="66" height="34" viewBox="0 0 66 34" aria-hidden="true">
        <g fill="none" stroke="#4a4a4a" stroke-width="5"><path d="M0 3l14 14L0 31"/><path d="M16 3l14 14-14 14"/><path d="M32 3l14 14-14 14"/><path d="M48 3l14 14-14 14"/></g>
      </svg>
    </div>

    <div class="contact">
      <p class="contact__line">
        <svg class="contact__icon" width="24" height="28" viewBox="0 0 24 28" aria-hidden="true"><path d="M7 2 3 5c-2 6 4 17 12 21l4-3-4-6-3 2c-3-2-5-6-6-10l3-2z" fill="none" stroke="#c9a949" stroke-width="2"/></svg>
        07 3000 1234
      </p>
      <p class="contact__line">
        <svg class="contact__icon" width="30" height="22" viewBox="0 0 30 22" aria-hidden="true"><g fill="none" stroke="#c9a949" stroke-width="2"><rect x="1" y="1" width="28" height="20"/><path d="M1 1l14 11L29 1M1 21l10-10M29 21 19 11"/></g></svg>
        0400 555 018
      </p>
    </div>

    <div class="brand">
      <span class="brand__dot"></span>
      <span class="brand__name">BRIGHTLINE WINDOW TINTING</span>
    </div>
    <p class="web">www.brightlinetinting.com.au</p>
  </section>

</main>
</body>
</html>
```